Daily Deals Website Needs a Landing Page (Home Page will act as the landing page)

We need a landing page for a daily deals website that will act as the home page. We have attached the wire frame and logo for reference. Open to creative ideas and suggestions as long as the main elements of the wireframe are incorporated in the design. Need a very simplistic design approach like Vorplex's search page. (www.vorplex.com) . Very clean and distinct CTA's.

Target Market(s)

Customers looking for deals on everyday use items

Font styles to use
Sans Serif

Requirements
Must have
• clean design, lots of white space and strong CTA .
Nice to have
• need a clean design overall. Strong CTA
Should not have
• Cluttered look. Too many colors, keep it simple

```html
<!DOCTYPE html>
<html lang="en">
<head>
<meta charset="utf-8">
<title>NEXORA – Daily Deals</title>
<link href="https://fonts.googleapis.com/css2?family=Ubuntu:wght@400;500;700&display=swap" rel="stylesheet">
<style>
  :root {
    --blue: #1e3399;
    --green: #63bf4f;
    --ink: #1b1b1b;
    --ghost: #e4e4e4;
    --badge: #f7b500;
    --footer: #f7f7f7;
    --white: #ffffff;
  }
  * { margin: 0; padding: 0; box-sizing: border-box; }
  html, body { width: 1200px; height: 686px; overflow: hidden; background: var(--white); }
  body { font-family: "Ubuntu", sans-serif; color: var(--ink); position: relative; }
  .page { position: absolute; inset: 5px 0 0 0; }
  .abs { position: absolute; }

  .brand { left: 0; width: 1200px; top: 52px; text-align: center; font-size: 30px; font-weight: 700; color: var(--blue); letter-spacing: 1px; }
  .tagline { left: 0; width: 1200px; top: 128px; text-align: center; font-size: 11px; }
  .signin-label { left: 0; width: 1200px; top: 186px; text-align: center; font-size: 9.5px; font-weight: 700; color: var(--blue); }
  .signin-btn { top: 216px; width: 31px; height: 31px; border: 1.5px solid var(--blue); border-radius: 5px; background: #f4fbf2; display: flex; align-items: center; justify-content: center; }

  .ghost { color: var(--ghost); font-weight: 500; line-height: 1; white-space: nowrap; }
  .ghost-small { font-size: 22px; }
  .ghost-big { font-size: 27px; }

  .deal-title { font-size: 13.5px; font-weight: 700; line-height: 15px; width: 150px; }
  .deal-title.blue { color: var(--blue); }
  .deal-title.green { color: var(--green); }
  .deal-text { font-size: 7.8px; line-height: 11.9px; width: 145px; }
  .explore { font-size: 9.5px; font-weight: 700; color: var(--green); }
  .explore::after { content: ""; position: absolute; left: 0; top: 17px; width: 18px; height: 1.5px; background: var(--green); }
  .photo { width: 172px; height: 172px; border-radius: 2px; box-shadow: 0 6px 14px rgba(0,0,0,0.12); }
  .photo-kitchen { background: linear-gradient(160deg, #7a4a26 0%, #c08a57 45%, #8a4f26 75%, #4a2512 100%); }
  .photo-chair { background: radial-gradient(circle at 50% 55%, #f4efe6 0%, #e6ebea 40%, #d8e0e0 100%); }
  .badge { left: 747px; top: 272px; width: 62px; height: 26px; background: var(--badge); color: var(--white); font-size: 7.5px; font-weight: 700; line-height: 8.5px; padding: 4px 0 0 26px; clip-path: polygon(0 0, 100% 0, 100% 100%, 0 100%, 14px 50%); }

  .new-here { left: 0; width: 1200px; top: 516px; text-align: center; font-size: 10px; }
  .signup { left: 542px; top: 541px; width: 116px; height: 32px; background: var(--blue); color: var(--green); border-radius: 3px; font-size: 11px; font-weight: 700; display: flex; align-items: center; justify-content: center; }

  .footer { left: 0; top: 620px; width: 1200px; height: 32px; background: var(--footer); }
  .social { top: 6px; width: 19px; height: 19px; border: 1px solid var(--blue); border-radius: 2px; background: #eef8ec; display: flex; align-items: center; justify-content: center; }
  .social span { width: 7px; height: 7px; border-radius: 50%; background: var(--green); }
  .footer-link { top: 10px; font-size: 10px; }
  .copyright { top: 10px; right: 88px; font-size: 10px; }
  .copyright b { color: var(--green); font-weight: 400; }
</style>
</head>
<body>
<main class="page">
  <div class="abs brand">NEXORA</div>
  <div class="abs tagline">Company Tagline Goes Here</div>

  <div class="abs signin-label">Sign In with:</div>
  <div class="abs signin-btn" style="left:563px" aria-label="Sign in with account">
    <svg width="12" height="12" viewBox="0 0 12 12"><circle cx="6" cy="6" r="5" fill="var(--green)"/></svg>
  </div>
  <div class="abs signin-btn" style="left:606px" aria-label="Sign in with email">
    <svg width="15" height="12" viewBox="0 0 15 12"><rect width="15" height="12" rx="1" fill="var(--green)"/><path d="M1.5 2 L7.5 6.5 L13.5 2" fill="none" stroke="#fff" stroke-width="1.4"/></svg>
  </div>

  <!-- Featured deal -->
  <div class="abs ghost ghost-small" style="left:128px; top:251px">FEATURED</div>
  <div class="abs ghost ghost-big" style="left:128px; top:268px">DEAL OF THE DAY</div>
  <h2 class="abs deal-title blue" style="left:229px; top:282px">Clean Modern<br>Kitchen Set</h2>
  <p class="abs deal-text" style="left:229px; top:322px">Lorem ipsum dolor sit amet, consetetur sadipscing elitr, sed diam nonumy eirmod tempor invidunt ut labore et dolore magna aliquyam erat, sed diam voluptua. At vero eos et accusam et justo duo dolores et</p>
  <a class="abs explore" style="left:229px; top:418px">Explore More</a>
  <svg class="abs" style="left:312px; top:419px" width="28" height="8" viewBox="0 0 28 8"><path d="M0 4 H27 M23 1 L27 4 L23 7" fill="none" stroke="var(--blue)" stroke-width="1.1"/></svg>
  <div class="abs photo photo-kitchen" style="left:391px; top:265px" role="img" aria-label="Photo of a modern wooden kitchen with an island"></div>

  <!-- Promoted deal -->
  <div class="abs photo photo-chair" style="left:637px; top:265px" role="img" aria-label="Photo of a white tufted armchair"></div>
  <div class="abs badge">30%<br>OFF</div>
  <div class="abs ghost ghost-small" style="left:799px; top:251px">PROMOTED</div>
  <div class="abs ghost ghost-big" style="left:799px; top:268px; clip-path: inset(0 0 0 10px)">DEAL OF THE DAY</div>
  <h2 class="abs deal-title green" style="left:828px; top:282px">Comfortable<br>Luxury Chair</h2>
  <p class="abs deal-text" style="left:828px; top:322px">Lorem ipsum dolor sit amet, consetetur sadipscing elitr, sed diam nonumy eirmod tempor invidunt ut labore et dolore magna aliquyam erat, sed diam voluptua. At vero eos et accusam et justo duo dolores et</p>
  <a class="abs explore" style="left:828px; top:418px">Explore More</a>
  <svg class="abs" style="left:911px; top:419px" width="28" height="8" viewBox="0 0 28 8"><path d="M0 4 H27 M23 1 L27 4 L23 7" fill="none" stroke="var(--blue)" stroke-width="1.1"/></svg>

  <div class="abs new-here">Are you new here? Let's create an account!</div>
  <a class="abs signup">Sign Up</a>

  <footer class="abs footer">
    <div class="abs social" style="left:88px"><span></span></div>
    <div class="abs social" style="left:113px"><span></span></div>
    <div class="abs social" style="left:138px"><span></span></div>
    <div class="abs social" style="left:163px"><span></span></div>
    <a class="abs footer-link" style="left:212px">Terms Of Service</a>
    <a class="abs footer-link" style="left:311px">Privacy Policy</a>
    <div class="abs copyright">Copyright © 2021 <b>NEXORA</b>. All rights reserved</div>
  </footer>
</main>
</body>
</html>
```